Business Card design for construction company

I would like a business card design for a construction company - Harlow Constructions. I have attached the ai logo file for use. I would like the card to be very smart and clean and incorporate only white and the two colours in the logo. I would like the card to have two sides. One side can just have the logo, the other with the relevant information.

Target Market(s)

Building and Construction Clients

Industry/Entity Type

Business

Contact Information for Business Card

Name: Tom Pardoe
Company: Harlow Constructions Pty Limited
Address: 14 Mallee Crescent Carrow Vale 2093
Phone: 0427 531 068
Email: tomp@harlowbuild-example.com.au

Font styles to use
Serif
Sans Serif

Requirements
Must have
• Details noted above
• Logo as provided
• Colours as in logo
• Square edges
• A font that compliments the logo
Should not have
• Any colour other than white and those in logo
• Rounded edges

```html
<!DOCTYPE html>
<html lang="en">
<head>
<meta charset="utf-8">
<title>Harlow Constructions – Business Card</title>
<link rel="stylesheet" href="https://fonts.googleapis.com/css2?family=Oswald:wght@300;400&display=swap">
<style>
  :root {
    --brand-blue: #00aeef;
    --brand-grey: #58595b;
    --paper: #ffffff;
    --trim: #c8c8c8;
    --text-dark: #3a3a3a;
  }
  html, body {
    margin: 0;
    padding: 0;
    width: 1200px;
    height: 738px;
    overflow: hidden;
    background: var(--paper);
  }
  .presentation {
    position: relative;
    width: 1200px;
    height: 738px;
    font-family: "Oswald", sans-serif;
  }
  .card {
    position: absolute;
    top: 106px;
    width: 463px;
    height: 299px;
    box-sizing: border-box;
    border: 1px solid var(--trim);
    background: var(--paper);
    overflow: hidden;
  }
  .card--front { left: 105px; }
  .card--back { left: 652px; }

  .wordmark {
    position: absolute;
    inset: 0;
    display: flex;
    align-items: center;
    justify-content: center;
    gap: 12px;
  }
  .wordmark__dot {
    width: 9px;
    height: 9px;
    background: var(--brand-blue);
  }
  .wordmark__name {
    font-weight: 300;
    font-size: 25px;
    letter-spacing: 3px;
    color: var(--brand-grey);
    text-transform: uppercase;
  }

  .card__accent {
    position: absolute;
    inset: 0;
    width: 100%;
    height: 100%;
  }
  .contact {
    position: absolute;
    left: 210px;
    top: 98px;
    color: var(--brand-grey);
  }
  .contact__name {
    margin: 0 0 6px;
    font-weight: 400;
    font-size: 29px;
    line-height: 34px;
    letter-spacing: 1.5px;
    text-transform: uppercase;
  }
  .contact__details {
    margin: 0;
    font-weight: 300;
    font-size: 15.5px;
    line-height: 22px;
  }

  .spec {
    position: absolute;
    left: 112px;
    top: 442px;
    margin: 0;
    font-weight: 300;
    font-size: 17px;
    color: var(--text-dark);
  }
  .palette {
    position: absolute;
    top: 540px;
    left: 178px;
    display: flex;
    gap: 20px;
  }
  .swatch {
    width: 107px;
    height: 107px;
    box-sizing: border-box;
  }
  .swatch--blue { background: var(--brand-blue); }
  .swatch--grey { background: var(--brand-grey); }
  .swatch--white { background: var(--paper); border: 1px solid var(--trim); }
</style>
</head>
<body>
  <main class="presentation">
    <section class="card card--front" aria-label="Card front">
      <div class="wordmark">
        <span class="wordmark__dot"></span>
        <span class="wordmark__name">Harlow Constructions</span>
      </div>
    </section>

    <section class="card card--back" aria-label="Card back">
      <svg class="card__accent" viewBox="0 0 461 297" aria-hidden="true">
        <rect x="0" y="0" width="14" height="297" fill="var(--brand-blue)"/>
        <rect x="186" y="98" width="4" height="128" fill="var(--brand-blue)"/>
      </svg>
      <div class="contact">
        <h1 class="contact__name">Tom Pardoe</h1>
        <p class="contact__details">
          Harlow Constructions Pty Limited<br>
          14 Mallee Crescent Carrow Vale 2093<br>
          0427 531 068<br>
          tomp@harlowbuild-example.com.au
        </p>
      </div>
    </section>

    <p class="spec">Size : 85 mm by 55 mm</p>

    <div class="palette" aria-label="Colour palette">
      <div class="swatch swatch--blue"></div>
      <div class="swatch swatch--grey"></div>
      <div class="swatch swatch--white"></div>
    </div>
  </main>
</body>
</html>
```